New Organic Skin Care Line Needs to Design a Product Label

***THE WINNER OF THIS PROJECT WILL MOST LIKELY BECOME THE EXCLUSIVE DESIGNER FOR OUR OTHER PRODUCT LABELS***

We need a label design for a new organic skin care product line called "Maple Dune Festoon." This specific product is a 100% pure organic coconut oil. It's used for skin hydration, protection, and makeup removal.

Info to include on front label:

1. Logo: Maple Dune Festoon (attached)
2. Product Name: Pure Coconut Oil (emphasize "organic" somewhere)
3. Slogan: Hydrate your skin and hair.
4. Size: 8 FL OZ 236mL

Attached is:

1. The brand logo "Maple Dune Festoon" with a white background.
2. An image of the bottle we will use.
3. An image of the bottle with lines to show the size and placement of the label.
4. The brand logo "Maple Dune Festoon" with a black background. (photoshop file)

What we need:

A simple mock up of the front side of the label on the bottle. We first want to know what it will look like on the bottle given the size and dimensions.

- We would like one label with a white background (including the logo with a white background).
- We would like a second label with a black background (including the logo with a black background, just need to make the black font white instead of black).

We can get a great idea of what to expect from the front side of the label so we will complete the back side once we identify a winner.
Updates

Apologies, but we are now using a different bottle. The previous one is now discontinued. Please view the two most recent images uploaded. One is an image of the new bottle by itself. The other is an image of that bottle with instructions. Please use your most recent designs on the new bottle. Feel free to make any modifications you see fit to compliment the new bottle shape. Added Friday, March 18, 2016

Project Deadline Extended
Reason: We are still working with the label company to finalize the size. Once the size is confirmed we will have to tweak labels based on finalized measurements.

Target Market(s)

Women, 18-70

Industry/Entity Type

Skin Care Product

Font styles to use
Decorative
Script

Requirements
Must have
• -"shabby sheek" and "cute" theme
• -soft organic feel
• -the ingredients are organic, pure, and natural. That should be an essence of the label.

```html
<!DOCTYPE html>
<html lang="en">
<head>
<meta charset="UTF-8">
<title>Maple Dune Festoon – Pure Coconut Oil Label</title>
<link href="https://fonts.googleapis.com/css2?family=Cinzel:wght@400;600&family=Great+Vibes&family=Fredoka:wght@600&family=Cormorant+Garamond:wght@500&display=swap" rel="stylesheet">
<style>
  :root {
    --page-cream: #fbf1da;
    --label-black: #0b0b0b;
    --label-pink: #e4145f;
    --label-pink-deep: #b50d47;
    --label-pink-light: #f43a7c;
    --gold: #f2b312;
    --gold-light: #ffe37a;
    --gold-deep: #c98400;
    --ink-white: #ffffff;
    --ink-cream: #f3ead8;
    --ink-dark: #3a1c00;
    --coconut-brown: #a65a26;
    --coconut-white: #f4f1e6;
    --leaf-green: #3f9b2d;
  }
  html, body {
    margin: 0;
    padding: 0;
    width: 1200px;
    height: 1200px;
    overflow: hidden;
    background: var(--page-cream);
  }
  .label-canvas {
    display: block;
    width: 1200px;
    height: 1200px;
  }
  .brand-name {
    font-family: "Cinzel", serif;
    font-weight: 400;
    font-size: 40px;
    letter-spacing: 9px;
    fill: var(--ink-cream);
  }
  .organic-claim-percent {
    font-family: "Fredoka", sans-serif;
    font-weight: 600;
    font-size: 30px;
    fill: var(--ink-white);
  }
  .organic-claim-word {
    font-family: "Great Vibes", cursive;
    font-size: 54px;
    fill: var(--ink-white);
  }
  .product-name {
    font-family: "Fredoka", sans-serif;
    font-weight: 600;
    font-size: 80px;
    fill: var(--ink-white);
  }
  .slogan {
    font-family: "Cinzel", serif;
    font-weight: 600;
    font-size: 26px;
    letter-spacing: 1px;
    fill: var(--ink-dark);
  }
  .net-size {
    font-family: "Cormorant Garamond", serif;
    font-weight: 500;
    font-size: 22px;
    letter-spacing: 1px;
    fill: var(--ink-white);
  }
</style>
</head>
<body>
<svg class="label-canvas" viewBox="0 0 1200 1200" xmlns="http://www.w3.org/2000/svg">
  <defs>
    <clipPath id="label-circle">
      <circle cx="600" cy="600" r="500"/>
    </clipPath>
    <linearGradient id="pink-field" x1="0" y1="0" x2="0" y2="1">
      <stop offset="0" stop-color="var(--label-pink-light)"/>
      <stop offset="0.5" stop-color="var(--label-pink)"/>
      <stop offset="1" stop-color="var(--label-pink-deep)"/>
    </linearGradient>
    <linearGradient id="gold-band" x1="0" y1="0" x2="1" y2="0">
      <stop offset="0" stop-color="var(--gold-deep)"/>
      <stop offset="0.5" stop-color="var(--gold)"/>
      <stop offset="0.8" stop-color="var(--gold-light)"/>
      <stop offset="1" stop-color="var(--gold)"/>
    </linearGradient>
    <linearGradient id="slogan-bar" x1="0" y1="0" x2="1" y2="0">
      <stop offset="0" stop-color="var(--gold)"/>
      <stop offset="0.5" stop-color="var(--gold-light)"/>
      <stop offset="1" stop-color="var(--gold)"/>
    </linearGradient>
    <radialGradient id="coconut-tones" cx="0.5" cy="0.5" r="0.5">
      <stop offset="0" stop-color="var(--coconut-white)"/>
      <stop offset="0.55" stop-color="var(--coconut-brown)"/>
      <stop offset="1" stop-color="var(--leaf-green)" stop-opacity="0"/>
    </radialGradient>
  </defs>

  <g class="round-label" clip-path="url(#label-circle)">
    <rect class="label-top-black" x="100" y="100" width="1000" height="1000" fill="var(--label-black)"/>
    <path class="label-pink-field"
          d="M100 440 C 300 420, 460 520, 640 470 C 800 430, 920 380, 1100 360 L1100 1100 L100 1100 Z"
          fill="url(#pink-field)"/>
    <path class="oil-wave-band"
          d="M100 430 C 300 410, 460 500, 640 455 C 800 410, 920 360, 1100 330 L1100 370 C 920 390, 800 440, 640 480 C 460 530, 300 430, 100 450 Z"
          fill="url(#gold-band)"/>
  </g>

  <text class="brand-name" x="600" y="375" text-anchor="middle">MAPLE DUNE FESTOON</text>

  <text class="organic-claim-percent" x="265" y="545">100%</text>
  <text class="organic-claim-word" x="235" y="585">Organic</text>

  <text class="product-name" x="600" y="670" text-anchor="middle">Pure Coconut Oil</text>

  <rect class="slogan-bar" x="275" y="695" width="590" height="42" fill="url(#slogan-bar)"/>
  <text class="slogan" x="570" y="725" text-anchor="middle">HYDRATE YOUR SKIN AND HAIR</text>

  <ellipse class="coconut-artwork" cx="560" cy="860" rx="210" ry="120"
           fill="url(#coconut-tones)" role="img"
           aria-label="Illustration of split coconut halves with green leaves"/>

  <line x1="520" y1="1020" x2="680" y2="1020" stroke="var(--ink-white)" stroke-width="1" opacity="0.6"/>
  <text class="net-size" x="600" y="1048" text-anchor="middle">8 FL OZ 236ML</text>
  <line x1="520" y1="1062" x2="680" y2="1062" stroke="var(--ink-white)" stroke-width="1" opacity="0.6"/>
</svg>
</body>
</html>
```